Design Creative Banner or Gif Ads. 3 Designs To Be Selected

Come up with some creative banner ads for stonewell.co.nz

*At least 3 different winning banners will be chosen*

Please provide banner ads / gif ads in common google ads / website banner formats.

They can be gif or static but must stand out while still maintaining clear clean text and visuals, with a premium professional feel (please avoid clip art or anything that gives a cheap message).

Please keep in mind that these will likely be small ads so text needs to be large and if there's there a lot of text then use multiple frames/ pages as submit as a gif.

Style
Minimal & clean lines
Architectural or realistic images
Avoid cartoon styles, clipart, or anything that looks cheap

Font
Nexa or Montserrat or similar

Tone
Premium, serious, trustworthy — fits new builds

Colours
Option 1: Deep Navy (trust & quality) & lighter blues and warm grey
Option 2: Open to bright colours to help the ads stand out, such as (but not limited to) bright pink with black, yellow, fluorescent green, provided the messaging is still done professionally.
Our logo is attached (Stone Well Logo)

Display Sizes
Ad specs for file sizes should be file formats like JPEG, GIF, and PNG, with animations limited to a max of 30 seconds or less.
We will need several different ad sizes provided for each of the 3 selected winning designs.

• Medium Rectangle: 300 × 250 pixels
• Leaderboard: 728 × 90 pixels
• Desktop Banner ad image: (640x360 pixels)
• Desktop Banner ad image 2: (300x600 pixels)
• Possibly one or two other sizes

Flexibility to be creative
The ad text, words, upper/lower case, layout, colour, theme, and images can be adjusted to how you think it will look best. The follow example ads are just examples of what we are after but we are keen to see what you can create.

Recommendations at this point:
1. Avoid text heavy
2. Looking for more Gif ads
3. Imaging: if possible use real stock photo's rather than AI

Themes:

1
Building Soon? Start Here
Free Build Planning Pack:
✓ Build Cost Calculator
✓ Hidden Cost Checklist
✓ Builder Comparison Guide
Build With Confidence
Download Free

2
Before You Choose A Builder
Compare Price, Scope, Risk & Value
Avoid Costly Mistakes
Choose The Right Builder With Confidence
Download The Free Guide

3
Planning A New Build?
Avoid These Common Mistakes:
✗ Hidden Exclusions
✗ Missing Scope
✗ Unrealistic Allowances
✗ Budget Blowouts
Download The Free Guide

4
Before You Buy Land
Know what it could cost to build.
Avoid Costly Building Mistakes
Download Our Free Guides

5
Know Your Build Budget?
• Free Build Cost Calculator
• Hidden Cost Checklist
• Build Planning Tools
Calculate Costs (Download)

Target Market(s)

Landowners looking to build

Industry/Entity Type

Building

Font styles to use
Other font styles liked:
• Nexa or Montserrat or similar

Requirements
Should not have
• Avoid cartoon styles, clipart, or anything that looks cheap

```html
<!DOCTYPE html>
<html lang="en">
<head>
<meta charset="utf-8">
<title>Stone Well — Banner Set</title>
<link href="https://fonts.googleapis.com/css2?family=Montserrat:wght@400;500;600;700;800;900&display=swap" rel="stylesheet">
<style>
  :root {
    --navy: #12344d;
    --navy-deep: #0e2c42;
    --blue: #2f8fc4;
    --sky: #4db6e4;
    --ink: #1a3a52;
    --paper: #f1f3f5;
    --white: #ffffff;
  }
  * { box-sizing: border-box; margin: 0; padding: 0; }
  html, body { width: 1200px; height: 562px; overflow: hidden; background: var(--white); }
  body { font-family: 'Montserrat', sans-serif; color: var(--ink); }

  .stage { position: absolute; left: 0; top: 0; width: 1920px; height: 900px; transform: scale(0.625); transform-origin: 0 0; }
  .size-label { position: absolute; font-size: 22px; font-weight: 500; color: #222; transform: translateX(-50%); }
  .banner { position: absolute; overflow: hidden; box-shadow: 0 14px 40px rgba(0,0,0,.14); }
  .abs { position: absolute; }
  .photo { position: absolute; }

  .brand { position: absolute; display: flex; align-items: center; gap: 12px; font-weight: 600; white-space: nowrap; }
  .brand-mark { width: 1em; height: 1em; }

  .btn { position: absolute; display: flex; align-items: center; justify-content: center; background: var(--sky); color: var(--white); border: 2px solid var(--white); border-radius: 5px; font-weight: 600; letter-spacing: .3px; }

  /* 640x360 */
  .wide { left: 263px; top: 100px; width: 640px; height: 360px; background: var(--paper); }
  .wide .photo { left: 300px; top: 0; width: 340px; height: 315px; background: linear-gradient(90deg, rgba(241,243,245,1) 0%, rgba(170,168,160,.6) 25%, #8d8a80 55%, #6b6a63 80%, #5f7a52 100%); }
  .wide .brand { left: 20px; top: 20px; font-size: 25px; color: var(--navy); }
  .wide .brand-mark { width: 48px; height: 44px; background: var(--navy); }
  .wide .headline { left: 21px; top: 80px; font-size: 37px; font-weight: 800; color: var(--blue); }
  .wide .sub { left: 21px; top: 124px; font-size: 26px; font-weight: 700; color: var(--navy); }
  .wide .sub-light { left: 21px; top: 155px; font-size: 20px; font-weight: 400; color: var(--navy); }
  .wide .pack { left: 22px; top: 195px; width: 430px; height: 105px; background: linear-gradient(90deg, var(--navy) 70%, rgba(18,52,77,0)); border-radius: 4px 0 0 4px; }
  .wide .pack-icon { left: 37px; top: 214px; width: 67px; height: 67px; border-radius: 50%; background: var(--sky); display: flex; align-items: center; justify-content: center; }
  .wide .pack-title { left: 116px; top: 204px; font-size: 18px; font-weight: 600; color: var(--sky); }
  .wide .checks { left: 116px; top: 231px; list-style: none; color: var(--white); font-size: 15px; line-height: 20px; }
  .checks li { display: flex; align-items: center; gap: 6px; }
  .tick { width: 13px; height: 13px; }
  .wide .btn { left: 358px; top: 225px; width: 149px; height: 45px; font-size: 16px; }
  .wide .footer { left: 0; top: 315px; width: 640px; height: 45px; background: var(--navy); color: var(--white); font-size: 17px; font-weight: 500; display: flex; align-items: center; justify-content: center; }
  .accent { color: var(--sky); font-weight: 700; }

  /* 300x250 */
  .rect { left: 983px; top: 99px; width: 300px; height: 250px; background: var(--navy); }
  .rect .photo { left: 150px; top: 0; width: 150px; height: 210px; background: linear-gradient(160deg, #e6a04a 0%, #c98a3e 30%, #9a7a55 55%, #d9d2c6 75%, #4f6e86 100%); clip-path: polygon(30px 0, 100% 0, 100% 100%, 0 100%); }
  .rect .slash { position: absolute; left: 144px; top: 0; width: 40px; height: 210px; background: var(--sky); clip-path: polygon(30px 0, 36px 0, 6px 100%, 0 100%); }
  .rect .brand { left: 15px; top: 14px; font-size: 16px; color: var(--white); gap: 8px; }
  .rect .brand-mark { width: 30px; height: 26px; background: var(--white); }
  .rect .headline { left: 15px; top: 48px; font-size: 20px; font-weight: 900; line-height: 22px; color: var(--sky); }
  .rect .lede { left: 15px; top: 97px; font-size: 16px; line-height: 21px; color: var(--white); }
  .rect .lede b { font-weight: 800; }
  .rect .btn { left: 16px; top: 149px; width: 168px; height: 46px; justify-content: flex-start; gap: 6px; padding-left: 6px; font-size: 13px; line-height: 15px; text-align: left; border-radius: 6px; }
  .rect .btn-icon { width: 36px; height: 36px; border-radius: 50%; background: var(--navy); display: flex; align-items: center; justify-content: center; flex-shrink: 0; }
  .rect .footer { left: 0; top: 210px; width: 300px; height: 40px; background: var(--sky); color: var(--navy); font-size: 12.5px; font-weight: 500; line-height: 15px; text-align: center; padding-top: 4px; }

  /* 300x600 */
  .tall { left: 1358px; top: 100px; width: 300px; height: 600px; background: var(--navy); }
  .tall .photo { left: 0; top: 130px; width: 300px; height: 390px; background: linear-gradient(180deg, #c9ccc9 0%, #a6a39b 30%, #7b776f 55%, #5b5a55 75%, #4c6a46 100%); }
  .tall .chevron { left: 0; top: 0; width: 300px; height: 200px; }
  .tall .brand { left: 75px; top: 16px; font-size: 17px; color: var(--white); gap: 9px; }
  .tall .brand-mark { width: 34px; height: 30px; background: var(--white); }
  .tall .center { left: 0; width: 300px; text-align: center; }
  .tall .headline { top: 58px; font-size: 27px; font-weight: 800; color: var(--sky); }
  .tall .lede { top: 92px; font-size: 18px; line-height: 24px; color: var(--white); font-weight: 500; }
  .tall .lede b { color: var(--sky); font-weight: 700; }
  .tall .panel { left: 15px; top: 352px; width: 270px; height: 129px; background: var(--navy); border-radius: 6px; }
  .tall .panel-note { top: 361px; font-size: 13px; line-height: 18px; color: var(--sky); font-weight: 500; }
  .tall .guide { left: 48px; top: 403px; display: flex; align-items: center; gap: 14px; color: var(--white); font-size: 19px; font-weight: 600; line-height: 21px; }
  .tall .guide-icon { width: 46px; height: 46px; border-radius: 50%; background: var(--sky); display: flex; align-items: center; justify-content: center; }
  .tall .btn { left: 55px; top: 460px; width: 192px; height: 44px; font-size: 16px; }
  .tall .rule { left: 0; top: 518px; width: 300px; height: 4px; background: var(--sky); }
  .tall .footer { top: 543px; font-size: 15px; line-height: 19px; color: var(--white); font-weight: 500; }
  .tall .footer b { color: var(--sky); font-size: 18px; font-weight: 700; }

  /* 728x90 */
  .leader { left: 263px; top: 610px; width: 728px; height: 90px; background: var(--paper); }
  .leader .photo { left: 330px; top: 0; width: 398px; height: 90px; background: linear-gradient(90deg, rgba(241,243,245,1) 0%, #b9c4c7 25%, #9fb1b6 55%, #c9b98a 80%, #d9a64a 100%); }
  .leader .mark { left: 60px; top: 18px; width: 33px; height: 28px; background: var(--navy); }
  .leader .brand { left: 20px; top: 48px; font-size: 19px; color: var(--navy); }
  .leader .headline { left: 153px; top: 10px; font-size: 23px; font-weight: 800; color: var(--blue); }
  .leader .lede { left: 153px; top: 41px; font-size: 14.5px; line-height: 19px; font-weight: 700; color: var(--navy); }
  .leader .offer { left: 532px; top: 19px; font-size: 16px; font-weight: 700; color: var(--navy); }
  .leader .btn { left: 550px; top: 40px; width: 138px; height: 34px; font-size: 16px; }
</style>
</head>
<body>
<div class="stage">

  <div class="size-label" style="left:583px; top:58px;">640x360</div>
  <div class="size-label" style="left:1133px; top:58px;">300x250</div>
  <div class="size-label" style="left:1502px; top:54px;">300x600</div>
  <div class="size-label" style="left:627px; top:567px;">700x90</div>

  <!-- 640x360 -->
  <section class="banner wide">
    <div class="photo" role="img" aria-label="Modern two-storey house at dusk with lit windows and landscaped garden"></div>
    <div class="brand"><span class="brand-mark"></span>Stone Well</div>
    <h2 class="abs headline">Bought Land?</h2>
    <p class="abs sub">Avoid Costly Build Mistakes</p>
    <p class="abs sub-light">Discover The Hidden Costs</p>
    <div class="abs pack"></div>
    <div class="abs pack-icon">
      <svg width="36" height="36" viewBox="0 0 36 36" fill="none" stroke="#12344d" stroke-width="2.4"><rect x="5" y="14" width="26" height="18" rx="2"/><rect x="3" y="9" width="30" height="6" rx="1.5"/><line x1="18" y1="9" x2="18" y2="32"/><path d="M18 9c-3-6-10-5-8 0M18 9c3-6 10-5 8 0"/></svg>
    </div>
    <p class="abs pack-title">Free Build Planning Pack</p>
    <ul class="abs checks">
      <li><svg class="tick" viewBox="0 0 14 14"><circle cx="7" cy="7" r="7" fill="#4db6e4"/><path d="M4 7.2l2 2 4-4" stroke="#fff" stroke-width="1.8" fill="none"/></svg>Build Cost Calculator</li>
      <li><svg class="tick" viewBox="0 0 14 14"><circle cx="7" cy="7" r="7" fill="#4db6e4"/><path d="M4 7.2l2 2 4-4" stroke="#fff" stroke-width="1.8" fill="none"/></svg>Build Journey Roadmap</li>
      <li><svg class="tick" viewBox="0 0 14 14"><circle cx="7" cy="7" r="7" fill="#4db6e4"/><path d="M4 7.2l2 2 4-4" stroke="#fff" stroke-width="1.8" fill="none"/></svg>Hidden Cost Checklist</li>
    </ul>
    <div class="btn">DOWNLOAD</div>
    <div class="abs footer">Choose The Right Builder With&nbsp;<span class="accent">Clarity &amp; Confidence.</span>&nbsp;Stone Well.</div>
  </section>

  <!-- 300x250 -->
  <section class="banner rect">
    <div class="photo" role="img" aria-label="Construction crane, stacked coins and a small model house"></div>
    <div class="slash"></div>
    <div class="brand"><span class="brand-mark"></span>Stone Well</div>
    <h2 class="abs headline">PLANNING A<br>NEW BUILD?</h2>
    <p class="abs lede">Calculate Your<br><b>BUILD COST</b></p>
    <div class="btn">
      <span class="btn-icon"><svg width="18" height="20" viewBox="0 0 18 20" fill="none" stroke="#fff" stroke-width="1.6"><rect x="2" y="1" width="14" height="18" rx="2"/><rect x="5" y="4" width="8" height="4"/><path d="M5 11h2M9 11h2M5 15h2M9 15h2"/></svg></span>
      <span>Free Build<br>Cost Calculator</span>
    </div>
    <div class="abs footer">Stone Well<br>Compare Quotes From Trusted Builders</div>
  </section>

  <!-- 300x600 -->
  <section class="banner tall">
    <div class="photo" role="img" aria-label="Modern two-storey house with balcony and garden"></div>
    <svg class="abs chevron" viewBox="0 0 300 200" preserveAspectRatio="none">
      <polygon points="0,0 300,0 300,130 150,190 0,130" fill="#12344d"/>
      <polygon points="0,130 150,182 300,130 300,140 150,192 0,140" fill="#4db6e4"/>
    </svg>
    <div class="brand"><span class="brand-mark"></span>Stone Well</div>
    <h2 class="abs center headline">Bought Land?</h2>
    <p class="abs center lede">Before You Choose<br>A Builder, <b>Read This.</b></p>
    <div class="abs panel"></div>
    <p class="abs center panel-note">Avoid Costly Mistakes, Budget<br>Blowouts, &amp; Contract Surprises.</p>
    <div class="abs guide">
      <span class="guide-icon"><svg width="26" height="22" viewBox="0 0 26 22" fill="none" stroke="#12344d" stroke-width="2"><path d="M3 5l10-3 10 3-10 3z"/><path d="M3 10l10 3 10-3M3 15l10 3 10-3"/></svg></span>
      <span>Free Build<br>Planning Guide</span>
    </div>
    <div class="btn">DOWNLOAD NOW</div>
    <div class="abs rule"></div>
    <p class="abs center footer">Choose The Right Builder With<br><b>Clarity &amp; Confidence.</b></p>
  </section>

  <!-- 728x90 -->
  <section class="banner leader">
    <div class="photo" role="img" aria-label="Hand sketching a city skyline with construction cranes"></div>
    <div class="abs mark"></div>
    <div class="brand">Stone Well</div>
    <h2 class="abs headline">Bought Land?</h2>
    <p class="abs lede">Understand The Steps To<br>Building Your New Home</p>
    <p class="abs offer">Free Build Roadmap</p>
    <div class="btn">DOWNLOAD</div>
  </section>

</div>
</body>
</html>
```